Geschäftspapiere für eine Zahnarztpraxis
Zielgruppe
Zahnarztpraxis
Aufgabenstellung
Ich wünsche mir wenige grafische Elemente auf der Vorderseite. Die Rückseite soll komplett mit einer Grafik gefüllt sein.
Die Datei die ich als Fototapete zur Verfügung stelle, muss nicht zwangsläufig in dem Designvorschlag enthalten sein. Die Tapeten machen einen Großteil der Inneneinrichtung meiner Praxis aus. Sie sind ein Wiedererkennungsmerkmal, daher dachte ich, es würde Sinn ergeben, diese zum Teil in das Design einfließen zu lassen.

```html
<!DOCTYPE html>
<html lang="de">
<head>
<meta charset="utf-8">
<title>Geschäftspapiere – Zahnarztpraxis Holmstedt &amp; Team</title>
<link rel="stylesheet" href="https://fonts.googleapis.com/css2?family=Open+Sans:wght@300;400;600&display=swap">
<style>
  :root {
    --bg: #e7e8e9;
    --paper: #ffffff;
    --teal: #3d8577;
    --teal-dark: #2f6d61;
    --ink: #55595c;
    --ink-light: #8d9194;
    --rule: #d9dcdd;
    --wall-a: #e9a3b7;
    --wall-b: #8fc7d6;
    --wall-c: #f2d27a;
    --wall-d: #b7a3d9;
    --wall-e: #9ed0a6;
  }
  * { box-sizing: border-box; margin: 0; padding: 0; }
  html, body { width: 1200px; height: 859px; overflow: hidden; }
  body {
    background: var(--bg);
    font-family: "Open Sans", Arial, sans-serif;
    color: var(--ink);
    position: relative;
  }
  .sheet, .envelope {
    position: absolute;
    background: var(--paper);
    box-shadow: 0 6px 18px rgba(0,0,0,.12);
    overflow: hidden;
  }
  .wallpaper {
    background:
      radial-gradient(circle at 15% 40%, var(--wall-a) 0, transparent 35%),
      radial-gradient(circle at 40% 70%, var(--wall-b) 0, transparent 35%),
      radial-gradient(circle at 62% 30%, var(--wall-c) 0, transparent 30%),
      radial-gradient(circle at 82% 65%, var(--wall-d) 0, transparent 35%),
      radial-gradient(circle at 95% 20%, var(--wall-e) 0, transparent 30%),
      linear-gradient(90deg, #f3c9d3, #cfe6ec, #f6e6b5, #dcd2ee);
  }

  /* Letterhead */
  .letterhead { left: 110px; top: 120px; width: 430px; height: 608px; }
  .letterhead .wallpaper-strip { position: absolute; left: 0; top: 0; width: 100%; height: 16px; }
  .brand { position: absolute; left: 38px; top: 48px; color: var(--teal); font-weight: 400; }
  .brand .practice { font-size: 6px; letter-spacing: 1.5px; text-transform: uppercase; }
  .brand .name { font-size: 13px; letter-spacing: 1.2px; text-transform: uppercase; margin-top: 1px; }
  .contact-block { position: absolute; left: 268px; top: 44px; font-size: 5.5px; line-height: 1.6; color: var(--ink-light); padding-left: 8px; border-left: 1px solid var(--teal); }
  .sender-line { position: absolute; left: 38px; top: 104px; font-size: 4.5px; color: var(--ink-light); border-bottom: .5px solid var(--rule); padding-bottom: 1px; }
  .letter-body { position: absolute; left: 38px; top: 170px; width: 340px; font-size: 6.3px; line-height: 1.7; }
  .letter-body p { margin-bottom: 7px; }
  .signature { width: 70px; height: 20px; margin: 6px 0 4px; background: linear-gradient(90deg, rgba(40,60,140,.35), rgba(40,60,140,.15)); border-radius: 10px; }
  .watermark-shape { position: absolute; left: 160px; top: 350px; width: 110px; height: 110px; border-radius: 50%; border: 1px solid #eef0f0; }
  .footer-columns { position: absolute; left: 38px; right: 38px; bottom: 34px; display: flex; justify-content: space-between; font-size: 5px; color: var(--ink-light); border-top: .5px solid var(--rule); padding-top: 6px; }
  .band { position: absolute; left: 0; bottom: 0; width: 100%; height: 16px; background: var(--teal); color: #fff; font-size: 5.5px; display: flex; align-items: center; justify-content: center; letter-spacing: .5px; }

  /* Envelopes */
  .envelope { width: 520px; height: 254px; left: 600px; }
  .envelope-back { top: 150px; }
  .envelope-back .flap { position: absolute; left: 0; top: 0; width: 100%; height: 64px; }
  .envelope-back .seam { position: absolute; left: 0; top: 64px; width: 100%; height: 1px; background: var(--rule); }
  .envelope-back .return-line { position: absolute; left: 0; right: 0; top: 150px; text-align: center; font-size: 5px; color: var(--ink-light); }
  .envelope-front { top: 440px; }
  .envelope-front .sender-line { left: 36px; top: 70px; }
  .window { position: absolute; left: 36px; top: 80px; width: 190px; height: 92px; border: 1px solid #d5d8d9; border-radius: 3px; background: #f4f5f5; }
  .envelope-front .band { height: 26px; }
  .envelope-front .wave { position: absolute; left: 0; bottom: 24px; width: 100%; height: 20px; }
</style>
</head>
<body>

<section class="sheet letterhead">
  <div class="wallpaper wallpaper-strip" role="img" aria-label="Bunter Ausschnitt der Praxis-Fototapete"></div>
  <div class="brand">
    <div class="practice">Zahnarztpraxis</div>
    <div class="name">Holmstedt &amp; Team</div>
  </div>
  <address class="contact-block">
    Zahnarztpraxis Holmstedt &amp; Team<br>
    Lindenallee 12<br>
    80331 München<br>
    T 089 123 456<br>
    info@holmstedt-team.de
  </address>
  <div class="sender-line">Holmstedt &amp; Team · Lindenallee 12 · 80331 München</div>
  <div class="watermark-shape"></div>
  <div class="letter-body">
    <p>Sehr geehrte Damen und Herren,</p>
    <p>vielen Dank für Ihren Besuch in unserer Praxis. Wir freuen uns, Sie als Patientin oder Patient begrüßen zu dürfen und begleiten Sie gern auf dem Weg zu gesunden Zähnen.</p>
    <p>Anbei erhalten Sie Ihren nächsten Termin sowie eine Übersicht der geplanten Behandlung. Bei Fragen erreichen Sie uns jederzeit telefonisch oder per E-Mail.</p>
    <p>Wir wünschen Ihnen bis dahin alles Gute.</p>
    <p>Mit freundlichen Grüßen</p>
    <div class="signature" role="img" aria-label="Handschriftliche Unterschrift"></div>
    <p>Lena Holmstedt<br>Zahnärztin</p>
  </div>
  <div class="footer-columns">
    <span>Lindenallee 12, 80331 München</span>
    <span>Telefon 089 123 456</span>
    <span>Mo–Fr 8–18 Uhr</span>
  </div>
  <div class="band">www.holmstedt-team.de</div>
</section>

<section class="envelope envelope-back">
  <div class="wallpaper flap" role="img" aria-label="Praxis-Fototapete mit bunten Farbflächen"></div>
  <div class="seam"></div>
  <div class="return-line">Zahnarztpraxis Holmstedt &amp; Team · Lindenallee 12 · 80331 München</div>
</section>

<section class="envelope envelope-front">
  <div class="sender-line">Holmstedt &amp; Team · Lindenallee 12 · 80331 München</div>
  <div class="window"></div>
  <svg class="wave" viewBox="0 0 520 20" preserveAspectRatio="none">
    <path d="M0 20 Q260 0 520 8 L520 20 Z" fill="var(--teal)"/>
  </svg>
  <div class="band">www.holmstedt-team.de</div>
</section>

</body>
</html>
```